Dance school theatre show, "History" poster design

We need a poster design for our dance school show called WA History 2009-2014. This is our 5th year anniversary and we are producing our annual theatre show over 3 nights, with a different show every night.
The poster has to be eye catching, vibrant, imaginative, sleek.
We are called the Wendell Alcott School of Dance.
We don't like templates, cheesy dance designs, dance sillhoettes etc,

we like to be portrayed as a forward thinking and professional company, which we would like to convey in our design. We cover most aspects of dance styles
Updates

http://files.pictovault.net/design_img/482715/630284/630284_5174093_482715_thumbnail.jpg please use this last years design as a basis for quality we require

hi guys, I've just been speaking to a designer friend and everyone appears to be using the same old stock images which have been used to death. I'm hoping for, ideally, quite a bit more creativity, please refer back to last years poster. Obviously it's not themed but you can understand the quality we're going for Regards Owen

Reason: amendments required including more photo manipulation techniques

sorry for the delay guys, I've been away for a couple of days, will be reviewing all designs in next 2 days

Target Market(s)

males and females in their 30-60s. Dancer's parents, teenagers who are friends of the school.

Industry/Entity Type

School

Font styles to use
Serif
Sans Serif

Colors
e34398
fefefe
e567a6
b768aa
d2a4cc
ebdbea
fbd4d5
000000

Requirements
Must have
• must have the Wendell Alcott School of Dance presents
WA History 2009-2014
www.waschoolofdance.co.uk website address added
must have 24-26th July 2014, Bramwell Lantern Theatre
we will upload our dance logo shortly
** nb the slight change to date **
Should not have
• Flowery fonts, cheap templates, dancer sillhoettes etc

```html
<!DOCTYPE html>
<html lang="en">
<head>
<meta charset="utf-8">
<title>WA History 2009-2014 — Wendell Alcott School of Dance</title>
<link rel="stylesheet" href="https://fonts.googleapis.com/css2?family=Quicksand:wght@300;400;500;700&display=swap">
<style>
  :root {
    --ink-dark: #342d30;
    --ink-deep: #231e20;
    --tone-light: rgba(205, 200, 201, 0.85);
    --tone-mid: rgba(150, 143, 145, 0.8);
    --tone-soft: rgba(115, 108, 110, 0.75);
    --paper: #fefefe;
    --soft-text: #d6d0d2;
    --url-text: #aaa2a5;
    --accent: #e3285e;
    --brand-pink: #e34398;
    --spot: rgba(150, 136, 55, 0.42);
  }
  * { margin: 0; padding: 0; box-sizing: border-box; }
  html, body {
    width: 848px;
    height: 1200px;
    overflow: hidden;
    background: var(--ink-dark);
  }
  .poster {
    position: relative;
    width: 848px;
    height: 1200px;
    overflow: hidden;
    font-family: "Quicksand", sans-serif;
    color: var(--paper);
  }
  .poster__photo {
    position: absolute;
    inset: 0;
    background:
      radial-gradient(ellipse 90px 70px at 110px 430px, var(--tone-light), transparent 75%),
      radial-gradient(ellipse 170px 90px at 90px 540px, var(--tone-light), transparent 75%),
      radial-gradient(ellipse 230px 70px at 200px 900px, var(--tone-mid), transparent 75%),
      radial-gradient(ellipse 110px 80px at 470px 1010px, var(--tone-mid), transparent 75%),
      radial-gradient(ellipse 210px 170px at 420px 230px, var(--tone-mid), transparent 72%),
      radial-gradient(ellipse 160px 110px at 330px 150px, var(--tone-soft), transparent 72%),
      radial-gradient(ellipse 120px 170px at 770px 480px, var(--tone-mid), transparent 72%),
      radial-gradient(ellipse 130px 100px at 750px 250px, var(--tone-soft), transparent 72%),
      radial-gradient(ellipse 160px 260px at 60px 760px, var(--tone-soft), transparent 75%),
      linear-gradient(180deg, #2e2729 0%, #3d3537 30%, #3a3234 70%, #2d2729 100%);
  }
  .poster__spot {
    position: absolute;
    left: 132px;
    top: 360px;
    width: 540px;
    height: 540px;
    border-radius: 50%;
    background: var(--spot);
  }
  .presenter {
    position: absolute;
    top: 56px;
    left: 0;
    width: 100%;
    text-align: center;
    font-size: 26px;
    font-weight: 300;
    color: var(--soft-text);
  }
  .presenter strong { font-weight: 500; color: var(--paper); }
  .show-title {
    position: absolute;
    top: 526px;
    left: 0;
    width: 100%;
    text-align: center;
    font-size: 100px;
    font-weight: 300;
    line-height: 1;
    padding-left: 8px;
  }
  .show-rule {
    position: absolute;
    top: 622px;
    left: 202px;
    width: 480px;
    height: 5px;
    background: var(--accent);
  }
  .show-years {
    position: absolute;
    top: 638px;
    left: 0;
    width: 100%;
    text-align: center;
    font-size: 100px;
    font-weight: 700;
    line-height: 1;
    letter-spacing: 2px;
    padding-left: 8px;
  }
  .show-details {
    position: absolute;
    top: 754px;
    left: 0;
    width: 100%;
    text-align: center;
    font-size: 25px;
    font-weight: 400;
  }
  .show-details strong { font-weight: 700; }
  .school-mark {
    position: absolute;
    top: 1072px;
    left: 0;
    width: 100%;
    display: flex;
    justify-content: center;
    align-items: center;
    gap: 10px;
    font-size: 20px;
    font-weight: 700;
    color: var(--brand-pink);
    text-transform: uppercase;
    letter-spacing: 1px;
  }
  .school-mark__dot {
    width: 16px;
    height: 16px;
    border-radius: 50%;
    background: var(--brand-pink);
  }
  .website {
    position: absolute;
    top: 1146px;
    left: 0;
    width: 100%;
    text-align: center;
    font-size: 24px;
    font-weight: 300;
    color: var(--url-text);
  }
</style>
</head>
<body>
  <main class="poster">
    <div class="poster__photo" role="img" aria-label="Soft-focus black and white photograph of two dancers in a close duet, one resting a hand on the other's shoulder"></div>
    <div class="poster__spot"></div>

    <p class="presenter">the <strong>Wendell Alcott School of Dance</strong> presents</p>

    <h1 class="show-title">WA History</h1>
    <div class="show-rule"></div>
    <p class="show-years">2009-2014</p>
    <p class="show-details"><strong>24-26th July 2014</strong> Bramwell Lantern Theatre</p>

    <div class="school-mark">
      <span class="school-mark__dot"></span>
      <span>Wendell Alcott</span>
    </div>

    <p class="website">www.waschoolofdance.co.uk</p>
  </main>
</body>
</html>
```